'Bright Ledger Hidden Keys' Book Cover

I need a professional book cover design for my new upcoming book that shows people how to get a high credit score.

Here are my two websites:

https://www.moneywordbank-lexa.info
https://moneywordbank-lexa.com/

I am looking for a clean, professional design that pops (emotional touch) and separates from the other books that are on the market. Cover aspect ratio 1:4 for Pagewisp version and 1:5 for the paperback version. Yellow or blue are good colors - but not must. See the basic examples that I provided. File delivery format PDF.

Book Title: Bright Ledger Hidden Keys
Byline: The Quick Lift And Mend Manual for Stellar Borrowing

Currently on Brindlecart pre-order:
https://www.brindlecart.example/Bright-Ledger-Hidden-Keys-Stellar-ebook/dp/Q48MPLRT71

I am the author of 36 published books on Brindlecart. My author profile is here:
brindlecart.example/author/gideonvarly

Targeted audience: People that want to improve or repair their bad credit score.

Target Market(s)

People/consumers in the US that want to improve or repair their credit score.

Industry/Entity Type

Consumer

Font styles to use
Sans Serif

Colors

Designer to choose colors to be used in the design.

Requirements
Must have
• Author name, Title, byline, and graphic element(s).
Nice to have
• - 2020 edition logo / batch

```html
<!DOCTYPE html>
<html lang="en">
<head>
<meta charset="utf-8">
<title>Bright Ledger Hidden Keys – Book Cover</title>
<link rel="stylesheet" href="https://fonts.googleapis.com/css2?family=Source+Sans+3:wght@400;600;700;800;900&display=swap">
<style>
  :root {
    --lime: #98fb1c;
    --lime-light: #d6ff3c;
    --ink: #111111;
    --white: #ffffff;
    --navy: #14204d;
    --gold: #c9a25a;
    --chart: #eaff2a;
    --card-blue: #1f7fe6;
    --card-deep: #1446c9;
  }
  * { margin: 0; padding: 0; box-sizing: border-box; }
  html, body { width: 1200px; height: 868px; overflow: hidden; }
  body {
    font-family: "Source Sans 3", sans-serif;
    color: var(--ink);
  }
  .cover {
    position: relative;
    width: 1200px;
    height: 868px;
    background:
      radial-gradient(ellipse 60% 55% at 28% 45%, var(--lime-light) 0%, rgba(214,255,60,0) 70%),
      radial-gradient(ellipse 45% 40% at 82% 62%, #e8ff3a 0%, rgba(232,255,58,0) 70%),
      var(--lime);
    overflow: hidden;
  }

  /* Back cover */
  .back-heading {
    position: absolute; left: 94px; top: 68px;
    font-size: 19px; font-weight: 700; letter-spacing: 3.2px;
  }
  .back-blurb {
    position: absolute; left: 94px; top: 103px; width: 401px;
    font-size: 16px; line-height: 21.1px; text-align: justify;
  }
  .back-author {
    position: absolute; left: 94px; top: 477px;
    font-size: 19px; font-weight: 700; letter-spacing: 3px;
  }
  .author-photo {
    position: absolute; left: 94px; top: 524px; width: 115px; height: 169px;
    background: var(--white);
  }
  .author-bio {
    position: absolute; left: 226px; top: 517px; width: 269px;
    font-size: 16px; line-height: 21.1px; text-align: justify;
  }
  .publisher-mark {
    position: absolute; left: 94px; top: 720px; width: 90px; height: 90px;
    border-radius: 50%; background: var(--navy); border: 5px solid var(--white);
    display: flex; align-items: center; justify-content: center;
    color: var(--gold); font-size: 15px; font-weight: 700; letter-spacing: 1px;
  }
  .code-panel {
    position: absolute; left: 363px; top: 720px; width: 188px; height: 112px;
    background: var(--white);
  }

  /* Spine */
  .spine-title, .spine-author {
    position: absolute; left: 601px;
    writing-mode: vertical-rl; white-space: nowrap;
    transform: translateX(-50%);
  }
  .spine-title {
    top: 72px; font-size: 25px; font-weight: 700; color: var(--white); letter-spacing: 0.3px;
  }
  .spine-author {
    top: 522px; font-size: 21px; font-weight: 600; letter-spacing: 6.5px;
  }
  .spine-mark {
    position: absolute; left: 589px; top: 790px; width: 24px; height: 24px;
    border-radius: 50%; background: var(--navy);
  }

  /* Front cover */
  .front-author {
    position: absolute; left: 906px; top: 66px; transform: translateX(-50%);
    font-size: 23px; font-weight: 700; letter-spacing: 5.5px; white-space: nowrap;
  }
  .front-art { position: absolute; left: 0; top: 0; }
  .title-line { font-family: "Source Sans 3", sans-serif; fill: var(--white); }
  .subtitle {
    position: absolute; left: 906px; top: 382px; transform: translateX(-50%);
    font-size: 27px; font-weight: 800; line-height: 37px; letter-spacing: 1.2px;
    text-align: center; white-space: nowrap;
  }
  .program {
    position: absolute; left: 906px; top: 804px; transform: translateX(-50%);
    font-size: 15px; font-weight: 700; letter-spacing: 2.6px; white-space: nowrap;
  }
</style>
</head>
<body>
<main class="cover">

  <!-- Back cover -->
  <h2 class="back-heading">BRIGHT LEDGER HIDDEN KEYS</h2>
  <p class="back-blurb">Lorem ipsum dolor sit amet, consectetuer adipiscing elit, sed diam nonummy nibh euismod tincidunt ut laoreet dolore magna aliquam erat volutpat. Ut wisi enim ad minim veniam, quis nostrud exerci tation ullamcorper suscipit lobortis nisl ut aliquip ex ea commodo consequat. Duis autem vel eum iriure dolor in hendrerit in vulputate velit esse molestie consequat, vel illum dolore eu feugiat nulla facilisis at vero eros et accumsan et iusto odio dignissim qui blandit praesent luptatum zzril delenit augue duis dolore te feugait nulla facilisi.<br>Lorem ipsum dolor sit amet, cons ectetuer adipiscing elit, sed diam nonummy nibh euismod tincidunt ut laoreet dolore magna aliquam erat volutpat. Ut wisi enim ad minim veniam, quis nostrud exerci tation ullamcorper suscipit lobortis nisl ut aliquip ex ea commodo consequat.<br>Lorem ipsum dolor sit amet, consectetuer adipiscing elit,</p>

  <h3 class="back-author">GIDEON VARLY</h3>
  <div class="author-photo"></div>
  <p class="author-bio">Lorem ipsum dolor sit amet, cons ectetuer adipiscing elit, sed diam nonummy nibh euismod tincidunt ut laoreet dolore magna aliquam erat volutpat. Ut wisi enim ad minim veniam, quis nostrud exerci tation ullamcorper suscipit lobortis nisl ut aliquip ex ea commodo consequat.</p>
  <div class="publisher-mark">VARLY</div>
  <div class="code-panel"></div>

  <!-- Spine -->
  <div class="spine-title">BRIGHT LEDGER HIDDEN KEYS</div>
  <div class="spine-author">GIDEON VARLY</div>
  <div class="spine-mark"></div>

  <!-- Front cover -->
  <div class="front-author">GIDEON VARLY</div>

  <svg class="front-art" width="1200" height="868" viewBox="0 0 1200 868">
    <defs>
      <linearGradient id="cardFill" x1="0" y1="1" x2="1" y2="0">
        <stop offset="0" stop-color="#6fd3ff"/>
        <stop offset="0.45" stop-color="var(--card-blue)"/>
        <stop offset="1" stop-color="var(--card-deep)"/>
      </linearGradient>
    </defs>

    <polyline class="growth-chart" fill="none" stroke="var(--chart)" stroke-width="3.5"
      points="700,624 742,549 780,579 839,527 871,545 940,480 1010,400 1048,364 1082,381 1132,314"/>
    <g fill="none" stroke="var(--chart)" stroke-width="3.5">
      <circle cx="700" cy="624" r="7"/><circle cx="742" cy="549" r="7"/>
      <circle cx="780" cy="579" r="7"/><circle cx="839" cy="527" r="7"/>
      <circle cx="1048" cy="364" r="7"/><circle cx="1082" cy="381" r="7"/>
      <circle cx="1132" cy="314" r="7"/>
    </g>

    <g role="img" aria-label="Illustration of a blue bank card flying upward with light streaks">
      <rect x="820" y="500" width="250" height="200" rx="16" fill="url(#cardFill)" opacity="0.95"
        transform="rotate(-40 945 600)"/>
    </g>

    <text class="title-line" x="703" y="209" textLength="403" lengthAdjust="spacingAndGlyphs"
      font-size="128" font-weight="900">BRIGHT</text>
    <text class="title-line" x="703" y="286" textLength="403" lengthAdjust="spacingAndGlyphs"
      font-size="72" font-weight="700">LEDGER HIDDEN</text>
    <text class="title-line" x="706" y="365" textLength="400" lengthAdjust="spacing"
      font-size="74" font-weight="900">KEYS</text>
  </svg>

  <p class="subtitle">The Quick Lift &amp; Mend Manual<br>for Stellar Borrowing</p>
  <p class="program">VARLY FINANCIAL LITERACY PROGRAM</p>
</main>
</body>
</html>
```